Gombrevo business card

Based on company logo and website given , to design a business card temple. Slogan "Your furry friends deserves the best"
Color style please refer to our website

```html
<!DOCTYPE html>
<html lang="en">
<head>
<meta charset="utf-8">
<title>Gombrevo business card</title>
<link href="https://fonts.googleapis.com/css2?family=Roboto:wght@400;500;700&display=swap" rel="stylesheet">
<style>
  :root {
    --page-bg: #e4e4e4;
    --brand-blue: #2367b3;
    --brand-gold: #b8ac2e;
    --card-white: #ffffff;
    --ink: #2b2b2b;
    --shadow: rgba(0, 0, 0, 0.28);
  }
  * { margin: 0; padding: 0; box-sizing: border-box; }
  html, body {
    width: 1200px; height: 848px; overflow: hidden;
    background: var(--page-bg);
    font-family: "Roboto", Arial, sans-serif;
  }
  .canvas { position: relative; width: 1200px; height: 848px; }
  .card {
    position: absolute; left: 311px; width: 554px; height: 300px;
    box-shadow: 0 3px 6px var(--shadow);
    overflow: hidden;
  }
  .card--front { top: 104px; background: var(--brand-blue); color: var(--card-white); }
  .card--back { top: 443px; background: var(--card-white); color: var(--ink); }

  .wordmark { position: absolute; font-weight: 500; line-height: 1; letter-spacing: -0.5px; }
  .card--front .wordmark { left: 270px; top: 158px; font-size: 46px; color: var(--card-white); }
  .card--back .wordmark { left: 35px; top: 44px; font-size: 46px; color: var(--brand-gold); }

  .social { position: absolute; left: 351px; top: 252px; display: flex; align-items: center; gap: 7px; font-size: 13px; }
  .social__mark { width: 11px; height: 11px; background: var(--card-white); border-radius: 2px; }

  .tab { position: absolute; left: 0; top: 160px; width: 9px; height: 26px; background: var(--brand-gold); border-radius: 0 5px 5px 0; }
  .person { position: absolute; left: 35px; top: 157px; }
  .person__name { font-size: 21px; font-weight: 700; color: var(--brand-gold); line-height: 1.1; }
  .person__role { font-size: 13px; color: var(--ink); margin-top: 2px; }
  .divider { position: absolute; left: 131px; top: 191px; width: 386px; height: 1px; background: var(--brand-gold); }

  .address { position: absolute; left: 364px; top: 149px; font-size: 12.5px; line-height: 17px; }
  .contacts { position: absolute; left: 364px; top: 204px; list-style: none; font-size: 12.5px; line-height: 17px; }
  .contacts li { display: flex; align-items: center; gap: 5px; }
  .contacts svg { width: 10px; height: 10px; flex: none; }
  .contacts .accent { color: var(--brand-gold); }
</style>
</head>
<body>
<div class="canvas">
  <section class="card card--front">
    <div class="wordmark">Gombrevo</div>
    <div class="social"><span class="social__mark"></span><span>/gombrevo</span></div>
  </section>

  <section class="card card--back">
    <div class="wordmark">Gombrevo</div>
    <div class="tab"></div>
    <div class="person">
      <div class="person__name">Daniel Hartley</div>
      <div class="person__role">Founder &amp; CEO</div>
    </div>
    <div class="divider"></div>
    <address class="address" style="font-style:normal">
      12/40 Larkin Street<br>Glenvale Vic 3150
    </address>
    <ul class="contacts">
      <li><svg viewBox="0 0 10 10"><path d="M2 1l2 2-1 1c.6 1.3 1.7 2.4 3 3l1-1 2 2-1.5 1.5C4 9 1 6 .5 2.5z" fill="var(--brand-gold)"/></svg>1800 437 219</li>
      <li><svg viewBox="0 0 10 10"><rect x="2.5" y="0.5" width="5" height="9" rx="1" fill="none" stroke="var(--brand-gold)"/></svg>+61 3 9016 4482</li>
      <li><svg viewBox="0 0 10 10"><rect x="0.5" y="2" width="9" height="6" fill="var(--brand-gold)"/><path d="M.5 2L5 5.5 9.5 2" fill="none" stroke="#fff" stroke-width=".8"/></svg>sales@gombrevo.com.au</li>
      <li><svg viewBox="0 0 10 10"><circle cx="5" cy="5" r="4.3" fill="none" stroke="var(--brand-gold)"/><path d="M.7 5h8.6M5 .7c-2 2.5-2 6 0 8.6M5 .7c2 2.5 2 6 0 8.6" fill="none" stroke="var(--brand-gold)" stroke-width=".7"/></svg><span>www.<span class="accent">gombrevo.com</span>.au</span></li>
    </ul>
  </section>
</div>
</body>
</html>
```